A stationary and business card desgn for a podiatry clinic

i require a stationary design for letter heads, envelopes, buisness cards.

it is for a new podiatry practise within a medical centre, that deals with all lower limb pathology and injury and foot related problems.

the colour scheme for my exisiting logo is orange blue and white. colours provided below.
i would like a white background for the buisness card.

the final design should portray health and wellbeing in a professional manner that still looks modern but sophisticated.

male and female, off all ethinical backgrounds aged between 30-80 years

Medical

• letter head.
need to include all contact details mentioned below.
need to also include ABN 53120978446

i prefer the logo on the top left hand corner and the contact info on the right. the address can be written in a sentence like form as the footer.

Business card
Front:

include logo provided.

clinic details on the front of the card.

Delphine Carrow
B.Pod

P: 7394 5186
F: 7394 5130
M: 0437 612 908
E: delphine@tavrin.com.au
W: www.tavrin.com.au

(may use icons to indicate contact type)

on back

Appointments:

lines to write dates, time etc.
(3-4 of these)
and a small photo of just the foot from the logo in coloured watermark.

Address:
Brackwell Medical Centre
47 Tallowin Street
Brackwell SA 5174
(this location infomation could be in smaller font at the bottom of the buisness card under a line, running in a sentence like fashion) or in the bottom left or right hand corner in a paragraph like you would write it on an envelope

however if you think a different lay out at the back will look better by all means i just need to have room for the appointment even if it is just lines/ space.

i also prefer square cards not rounded corners.

thanks
• plain texts such as times new roman and arial

```html
<!DOCTYPE html>
<html lang="en">
<head>
<meta charset="utf-8">
<title>Tavrin Podiatry — Stationery Set</title>
<link href="https://fonts.googleapis.com/css2?family=Varela+Round&display=swap" rel="stylesheet">
<style>
  :root {
    --blue: #1b3f9f;
    --orange: #ee7420;
    --white: #ffffff;
    --ink: #3a3a3a;
    --backdrop: #b98247;
    --shadow: rgba(40, 20, 0, 0.35);
    --window: #d9d9d9;
    --faint-blue: rgba(110, 115, 160, 0.35);
    --faint-orange: rgba(238, 150, 90, 0.3);
  }
  * { margin: 0; padding: 0; box-sizing: border-box; }
  html, body { width: 1200px; height: 801px; overflow: hidden; }
  body {
    background: var(--backdrop);
    font-family: "Varela Round", Arial, sans-serif;
    color: var(--ink);
    position: relative;
  }
  .sheet {
    position: absolute;
    background: var(--white);
    box-shadow: 0 3px 8px var(--shadow);
    overflow: hidden;
  }

  /* Brand name */
  .brand {
    color: var(--blue);
    font-weight: 400;
    line-height: 1;
    display: flex;
    align-items: center;
    gap: 0.3em;
    white-space: nowrap;
  }
  .brand .dot {
    width: 0.7em; height: 0.7em;
    border-radius: 50%;
    background: var(--orange);
    flex: none;
  }

  .watermark {
    position: absolute;
    border-radius: 50%;
    background: radial-gradient(ellipse at 35% 60%, var(--faint-blue), transparent 55%),
                radial-gradient(ellipse at 65% 45%, var(--faint-orange), transparent 60%);
  }

  .band { position: absolute; left: 0; bottom: 0; width: 100%; display: block; }

  /* Business card front */
  .card-front { left: 115px; top: 170px; width: 142px; height: 82px; }
  .card-front .brand { position: absolute; left: 5px; top: 8px; font-size: 9px; }
  .card-front .holder { position: absolute; left: 98px; top: 13px; color: var(--orange); font-size: 4.6px; line-height: 1.4; white-space: nowrap; }
  .card-front .holder small { display: block; font-size: 3.6px; }
  .card-front .panel { position: absolute; left: 0; top: 46px; width: 100%; height: 36px; background: var(--blue); color: var(--white); }
  .card-front .notch { position: absolute; left: 12px; top: -1px; width: 0; height: 0; border-left: 4px solid transparent; border-right: 4px solid transparent; border-top: 4px solid var(--white); }
  .card-front .contacts { position: absolute; left: 5px; top: 5px; list-style: none; font-size: 3.8px; line-height: 5.2px; }
  .card-front .contacts li { display: flex; align-items: center; gap: 2px; white-space: nowrap; }
  .card-front .contacts svg { width: 3.5px; height: 3.5px; fill: var(--white); }
  .card-front .address { position: absolute; left: 85px; top: 6px; font-size: 3.6px; line-height: 5px; font-style: normal; white-space: nowrap; }
  .card-front .web { position: absolute; bottom: 2px; width: 100%; text-align: center; font-size: 3.6px; }

  /* Business card back */
  .card-back { left: 274px; top: 170px; width: 143px; height: 82px; }
  .card-back .note { position: absolute; left: 5px; top: 6px; font-size: 4px; display: flex; gap: 2px; align-items: flex-end; }
  .card-back .note span.line { display: inline-block; width: 28px; border-bottom: 0.5px solid var(--ink); }
  .card-back .web { position: absolute; bottom: 4px; width: 100%; text-align: center; font-size: 3.6px; }

  /* Compliments slip */
  .slip { left: 156px; top: 287px; width: 389px; height: 169px; }
  .slip .brand { position: absolute; left: 9px; top: 18px; font-size: 20px; }
  .slip .window { position: absolute; left: 8px; top: 96px; width: 130px; height: 56px; border-radius: 6px; background: radial-gradient(ellipse at center, #f4f4f4, var(--window)); box-shadow: inset 0 0 3px rgba(0,0,0,0.2); }

  /* Envelopes */
  .envelope { width: 389px; height: 170px; }
  .envelope-square { left: 85px; top: 473px; }
  .envelope-point { left: 154px; top: 566px; }
  .flap { position: absolute; left: 0; top: 0; width: 100%; height: 100%; }
  .envelope .brand { position: absolute; left: 50%; transform: translateX(-50%); font-size: 9px; }
  .envelope-square .brand { top: 22px; }
  .envelope-point .brand { top: 24px; }

  /* Letterhead */
  .letterhead { left: 573px; top: 40px; width: 529px; height: 681px; }
  .letterhead .brand { position: absolute; left: 50%; top: 30px; transform: translateX(-50%); font-size: 22px; }
  .letterhead .watermark { left: 99px; top: 229px; width: 360px; height: 242px; }
  .letterhead .contacts { position: absolute; right: 8px; top: 633px; list-style: none; font-size: 7px; line-height: 10px; color: #222; }
  .letterhead .contacts li { display: flex; align-items: center; gap: 4px; white-space: nowrap; }
  .letterhead .contacts svg { width: 7px; height: 7px; fill: #333; flex: none; }
</style>
</head>
<body>

<svg width="0" height="0" style="position:absolute" aria-hidden="true">
  <symbol id="icon-fax" viewBox="0 0 10 10"><rect x="2" y="0.5" width="6" height="3"/><rect x="0.5" y="3.5" width="9" height="5" rx="1"/><rect x="2.5" y="8" width="5" height="1.5"/></symbol>
  <symbol id="icon-phone" viewBox="0 0 10 10"><path d="M0.5 3 Q5 0 9.5 3 L8 5 L6.5 4 L3.5 4 L2 5 Z"/><rect x="2" y="5.5" width="6" height="4" rx="1"/></symbol>
  <symbol id="icon-mobile" viewBox="0 0 10 10"><path d="M3 0.5 h4 a1 1 0 0 1 1 1 v7 a1 1 0 0 1 -1 1 h-4 a1 1 0 0 1 -1 -1 v-7 a1 1 0 0 1 1 -1 Z M3.3 1.8 v5.6 h3.4 v-5.6 Z"/></symbol>
  <symbol id="icon-mail" viewBox="0 0 10 10"><path d="M0.5 2 h9 v6 h-9 Z M1.3 2.8 L5 5.6 L8.7 2.8 v4.4 h-7.4 Z"/></symbol>
  <symbol id="band-path" viewBox="0 0 100 2" preserveAspectRatio="none"><rect x="0" y="0" width="34" height="2" fill="#ee7420"/><polygon points="33,2 35,0 100,0 100,2" fill="#1b3f9f"/></symbol>
</svg>

<section class="sheet card-front" aria-label="Business card front">
  <div class="brand"><span class="dot"></span>Tavrin Podiatry</div>
  <p class="holder">Delphine Carrow<small>B.Pod</small></p>
  <div class="panel">
    <span class="notch"></span>
    <ul class="contacts">
      <li><svg><use href="#icon-fax"/></svg>7394 5130</li>
      <li><svg><use href="#icon-phone"/></svg>7394 5186</li>
      <li><svg><use href="#icon-mobile"/></svg>0437 612 908</li>
      <li><svg><use href="#icon-mail"/></svg>delphine@tavrin.com.au</li>
    </ul>
    <address class="address">Brackwell Medical Centre<br>47 Tallowin Street<br>Brackwell SA 5174</address>
    <p class="web">www.tavrin.com.au</p>
  </div>
</section>

<section class="sheet card-back" aria-label="Business card back">
  <p class="note">Note : <span class="line"></span></p>
  <div class="watermark" style="left:55px;top:8px;width:60px;height:26px" role="img" aria-label="Faint clinic watermark"></div>
  <div class="watermark" style="left:5px;top:38px;width:60px;height:28px" role="img" aria-label="Faint clinic watermark"></div>
  <p class="web">www.tavrin.com.au</p>
</section>

<section class="sheet slip" aria-label="Window compliments slip">
  <div class="brand"><span class="dot"></span>Tavrin Podiatry</div>
  <div class="watermark" style="left:180px;top:14px;width:200px;height:140px" role="img" aria-label="Faint clinic watermark"></div>
  <div class="window"></div>
  <svg class="band" height="5" viewBox="0 0 100 2" preserveAspectRatio="none"><use href="#band-path"/></svg>
</section>

<section class="sheet envelope envelope-square" aria-label="Envelope with straight flap">
  <svg class="flap" viewBox="0 0 389 170" preserveAspectRatio="none" aria-hidden="true">
    <path d="M0 0 H389 V40 Q389 50 379 50 H10 Q0 50 0 40 Z" fill="#fff" stroke="#cfcfcf" stroke-width="1"/>
  </svg>
  <div class="brand"><span class="dot"></span>Tavrin Podiatry</div>
</section>

<section class="sheet envelope envelope-point" aria-label="Envelope with pointed flap">
  <svg class="flap" viewBox="0 0 389 169" preserveAspectRatio="none" aria-hidden="true">
    <path d="M0 0 H389 V22 Q389 32 378 34 L200 62 Q194 63 188 62 L11 34 Q0 32 0 22 Z" fill="#fff" stroke="#cfcfcf" stroke-width="1"/>
  </svg>
  <div class="brand"><span class="dot"></span>Tavrin Podiatry</div>
</section>

<section class="sheet letterhead" aria-label="Letterhead">
  <div class="brand"><span class="dot"></span>Tavrin Podiatry</div>
  <div class="watermark" role="img" aria-label="Faint clinic watermark"></div>
  <ul class="contacts">
    <li><svg><use href="#icon-fax"/></svg>7394 5130</li>
    <li><svg><use href="#icon-phone"/></svg>7394 5186</li>
    <li><svg><use href="#icon-mobile"/></svg>0437 612 908</li>
    <li><svg><use href="#icon-mail"/></svg>delphine@tavrin.com.au</li>
  </ul>
  <svg class="band" height="5" viewBox="0 0 100 2" preserveAspectRatio="none"><use href="#band-path"/></svg>
</section>

</body>
</html>
```